" Prestando serviços especializados de advocacia, em especial nas áreas de Direito médico, terceiro setor e responsabilidade civil em virtude de acidente de trânsito "

```html
<!DOCTYPE html>
<html lang="pt-BR">
<head>
<meta charset="UTF-8">
<title>Assinatura de e-mail — Moreira &amp; Moreira Advogados Associados</title>
<link rel="stylesheet" href="https://fonts.googleapis.com/css2?family=Open+Sans:wght@400;600&display=swap">
<style>
  :root {
    --backdrop: #ececec;
    --paper: #ffffff;
    --ink: #2f2f2f;
    --ink-soft: #555555;
    --icon: #777777;
    --rule: #3a3a3a;
    --gold: #b8893a;
    --gold-light: #e3c27a;
    --gold-dark: #8a5f1e;
  }
  * { box-sizing: border-box; margin: 0; padding: 0; }
  html, body {
    width: 1200px; height: 1200px; overflow: hidden;
    background: var(--backdrop);
    font-family: "Open Sans", Arial, sans-serif;
    color: var(--ink);
  }
  .canvas {
    width: 1200px; height: 1200px;
    display: flex; align-items: center; justify-content: center;
  }
  .signature {
    position: relative;
    width: 1100px; height: 300px;
    background: var(--paper);
    box-shadow: 0 2px 10px rgba(0,0,0,0.08);
  }
  .signer {
    position: absolute; left: 44px; top: 30px;
    font-size: 21px; line-height: 30px; color: var(--ink);
  }
  .firm-mark {
    position: absolute; left: 44px; top: 140px;
    width: 480px;
    display: flex; align-items: center; gap: 16px;
  }
  .firm-mark__dot {
    width: 44px; height: 44px; border-radius: 50%;
    background: var(--gold);
    flex: none;
  }
  .firm-mark__name {
    font-weight: 400; font-size: 19px; line-height: 26px;
    color: var(--ink);
  }
  .divider {
    position: absolute; left: 560px; top: 110px;
    width: 2px; height: 160px; background: var(--rule);
  }
  .contact {
    position: absolute; left: 600px; top: 110px;
    list-style: none;
    font-size: 18px; line-height: 32px; color: var(--ink-soft);
  }
  .contact li { display: flex; align-items: center; gap: 14px; white-space: nowrap; }
  .contact li.contact__cont { padding-left: 32px; }
  .contact svg { width: 18px; height: 18px; flex: none; fill: var(--icon); }
  .gold-bar {
    position: absolute; right: 48px; top: 110px;
    width: 22px; height: 162px;
    background: linear-gradient(180deg, var(--gold-light) 0%, var(--gold) 45%, var(--gold-dark) 100%);
  }
</style>
</head>
<body>
<main class="canvas">
  <section class="signature">
    <p class="signer">Nome Sobrenome<br>OAB 33333</p>

    <div class="firm-mark">
      <span class="firm-mark__dot"></span>
      <p class="firm-mark__name">Moreira &amp; Moreira Advogados Associados</p>
    </div>

    <span class="divider"></span>

    <ul class="contact">
      <li>
        <svg viewBox="0 0 24 24" aria-hidden="true"><path d="M12 2a7 7 0 0 0-7 7c0 5 7 13 7 13s7-8 7-13a7 7 0 0 0-7-7zm0 9.5A2.5 2.5 0 1 1 12 6.5a2.5 2.5 0 0 1 0 5z"/></svg>
        Rua das Palmeiras, nº14, sala 03, Ed. Aurora
      </li>
      <li class="contact__cont">Centro - Itaberaba/BA</li>
      <li>
        <svg viewBox="0 0 24 24" aria-hidden="true"><path d="M6.6 10.8a15 15 0 0 0 6.6 6.6l2.2-2.2a1 1 0 0 1 1-.25 11.4 11.4 0 0 0 3.6.57 1 1 0 0 1 1 1V20a1 1 0 0 1-1 1A17 17 0 0 1 3 4a1 1 0 0 1 1-1h3.5a1 1 0 0 1 1 1c0 1.25.2 2.45.57 3.57a1 1 0 0 1-.25 1z"/></svg>
        7530001234
      </li>
      <li>
        <svg viewBox="0 0 24 24" aria-hidden="true"><path d="M12 2a10 10 0 1 0 0 20 10 10 0 0 0 0-20zm-1.5 14.5L6 12l1.4-1.4 3.1 3.1 6.1-6.1L18 9z"/></svg>
        Moreira &amp; Moreira Advogados associados
      </li>
      <li>
        <svg viewBox="0 0 24 24" aria-hidden="true"><path d="M3 5h18a1 1 0 0 1 1 1v12a1 1 0 0 1-1 1H3a1 1 0 0 1-1-1V6a1 1 0 0 1 1-1zm1 2v.4l8 5 8-5V7zm0 2.8V17h16V9.8l-8 5z"/></svg>
        administrativo@moreiraemoreira.com.br
      </li>
    </ul>

    <span class="gold-bar"></span>
  </section>
</main>
</body>
</html>
```